依頼詳細
タワーマンションの理事長にチラシを配布しようと思っています。そのチラシデザイン制作をお願いします。見る人が思わず参加したくなるようなインパクトのあるデザインをお願いします。
記載項目
社名:株式会社MN建築設計/電話:06-4827-3956/URL:http://mn-kenchiku.co.jp
サイズ
A4
ページ数
両面
希望イメージ
シンプル 複雑
単色 カラフル
暗い 明るい
日常 高級
遊び心 厳粛
未来的 伝統的
女性的 男性的

弊社のイメージカラーに合っていたこと、内容が見やすくて分かりやすかった為

このたびは短い期間でありながらもご参加いただきありがとうございました。
皆様の提案は全て良かったので選定に苦慮いたしました。今回選定されなかったご提案者様は残念な結果となりましたが、今後もご提案をお願いするときには是非参加くださいますようお願い申し上げます。

```html
<!DOCTYPE html>
<html lang="ja">
<head>
<meta charset="utf-8">
<title>タワーマンション管理組合 交流会</title>
<link href="https://fonts.googleapis.com/css2?family=Noto+Sans+JP:wght@400;500;700;900&family=Noto+Serif+JP:wght@700;900&display=swap" rel="stylesheet">
<style>
:root{
  --blue:#1b7fc4;
  --navy:#123a6b;
  --sky-top:#b9dcf1;
  --sky-bottom:#eef7fc;
  --red:#d6261f;
  --ink:#222;
  --paper:#ffffff;
  --line:#1b7fc4;
}
*{margin:0;padding:0;box-sizing:border-box}
html,body{width:846px;height:1200px;overflow:hidden;background:var(--paper)}
body{font-family:"Noto Sans JP",sans-serif;color:var(--ink)}
.flyer{position:relative;width:846px;height:1200px;overflow:hidden;background:var(--paper)}
.hero-photo{position:absolute;left:0;top:0;width:846px;height:720px;
  background:linear-gradient(180deg,var(--sky-bottom) 0%,var(--sky-top) 45%,#8fb6cf 70%,#6fa25a 88%,#4f8a3c 100%)}
.kicker{position:absolute;left:270px;top:22px;width:306px;height:40px;background:var(--blue);color:#fff;
  font-weight:700;font-size:21px;letter-spacing:2px;text-align:center;line-height:40px;border-radius:4px}
.title{position:absolute;left:0;width:846px;top:62px;text-align:center;font-family:"Noto Serif JP",serif;
  font-weight:900;font-size:104px;color:var(--blue);letter-spacing:10px;line-height:1.1}
.subtitle{position:absolute;left:0;width:846px;top:188px;text-align:center;font-family:"Noto Serif JP",serif;
  font-weight:700;font-size:30px;color:var(--navy);letter-spacing:3px}
.bubble{position:absolute;border-radius:50%;background:rgba(255,255,255,.9);border:2px solid #9cc6e3;
  display:flex;align-items:center;justify-content:center;text-align:center;font-size:15px;font-weight:500;color:var(--navy);line-height:1.4}
.band{position:absolute;left:0;top:655px;width:846px;height:62px;background:linear-gradient(90deg,rgba(40,90,40,0),rgba(40,90,40,.55) 20%,rgba(40,90,40,.55) 80%,rgba(40,90,40,0));
  color:#fff;font-family:"Noto Serif JP",serif;font-weight:900;font-size:40px;text-align:center;line-height:62px;letter-spacing:3px;
  text-shadow:0 0 4px var(--navy),0 0 2px var(--navy)}
.notice{position:absolute;left:40px;top:742px;width:490px}
.notice h3{font-size:16px;color:var(--blue);font-weight:700;margin-bottom:4px}
.notice p{font-size:11px;line-height:1.6}
.info-row{position:absolute;left:40px;display:flex;align-items:center;gap:16px}
.info-label{width:56px;height:56px;flex:none;background:var(--blue);color:#fff;border-radius:8px;font-weight:700;font-size:16px;
  display:flex;align-items:center;justify-content:center;writing-mode:vertical-rl;letter-spacing:2px}
.date{font-size:40px;font-weight:900;color:var(--navy);line-height:52px}
.time{font-size:20px;font-weight:700;color:var(--navy);line-height:26px;padding-left:220px}
.capacity{font-size:32px;font-weight:900;color:var(--navy);line-height:56px}
.venue-name{font-size:28px;font-weight:900;color:var(--navy);line-height:36px}
.venue-addr{font-size:14px;font-weight:500;line-height:20px}
.deadline{position:absolute;left:40px;top:1068px;font-size:27px;font-weight:900;color:var(--red);line-height:36px}
.program{position:absolute;left:560px;top:742px;width:250px;height:370px;border:2px solid var(--line);border-radius:12px;padding:44px 16px 14px;background:#fff}
.program-title{position:absolute;left:18px;right:18px;top:12px;text-align:center;font-weight:700;color:var(--blue);font-size:17px}
.slot{margin-top:10px}
.slot-time{font-size:22px;font-weight:900;color:var(--navy)}
.slot-part{font-size:12px;font-weight:700;color:var(--red)}
.slot-name{font-size:17px;font-weight:900;color:var(--navy)}
.slot-desc{font-size:11px;line-height:1.5;margin-top:3px}
.host{position:absolute;left:0;width:846px;top:1158px;text-align:center;font-size:14px;font-weight:700;color:var(--navy)}
.contact-tab{position:absolute;right:0;top:1130px;width:92px;height:70px;background:var(--navy);color:#fff;font-size:12px;font-weight:700;
  display:flex;flex-direction:column;align-items:center;justify-content:center;line-height:1.5}
</style>
</head>
<body>
<main class="flyer">
  <div class="hero-photo" role="img" aria-label="青空の下にそびえるタワーマンション群と手前の緑の木々の写真"></div>

  <div class="kicker">タワーマンション管理組合</div>
  <h1 class="title">交流会</h1>
  <p class="subtitle">管理組合の自立を目指す</p>

  <div class="bubble" style="left:40px;top:250px;width:108px;height:108px">他のタワー<br>マンション<br>はどう?</div>
  <div class="bubble" style="left:60px;top:380px;width:100px;height:100px">管理費の<br>値上げ?</div>
  <div class="bubble" style="left:60px;top:500px;width:118px;height:118px">理事のなり手<br>がいない<br>どうする?</div>
  <div class="bubble" style="left:690px;top:320px;width:106px;height:106px">修繕費が<br>高くない?</div>
  <div class="bubble" style="left:690px;top:450px;width:106px;height:106px">民泊問題<br>はどう?</div>

  <div class="band">タワーマンションの未来を考える</div>

  <section class="notice">
    <h3>新型コロナウイルス対策について</h3>
    <p>交流会は新型コロナウイルスの感染防止に十分配慮して実施いたします。入室時の検温と手指消毒、マスクの着用にご協力ください。体調の優れない方は参加をお控えください。</p>
  </section>

  <div class="info-row" style="top:828px">
    <div class="info-label">日時</div>
    <div><div class="date">2022年6月5日(日)</div><div class="time">10:00～12:00</div></div>
  </div>
  <div class="info-row" style="top:924px">
    <div class="info-label">定員</div>
    <div class="capacity">先着15名様</div>
  </div>
  <div class="info-row" style="top:996px">
    <div class="info-label">会場</div>
    <div><div class="venue-name">緑ヶ丘スカイレジデンス</div><div class="venue-addr">大阪府大阪市中央区緑町3丁目4番12号</div></div>
  </div>

  <p class="deadline">申込締切：2022年5月22日(日)</p>

  <aside class="program">
    <div class="program-title">交流会の内容</div>
    <div class="slot">
      <div class="slot-time">10:00～10:50</div>
      <div class="slot-part">第1部</div>
      <div class="slot-name">意見交流会(全員参加型)</div>
      <div class="slot-desc">参加者の方々で、課題を共有し、解決策を検討します。</div>
    </div>
    <div class="slot" style="margin-top:22px">
      <div class="slot-time">10:50～11:50</div>
      <div class="slot-part">第2部</div>
      <div class="slot-name">修繕工事の進め方と考え方</div>
      <div class="slot-desc">講師　三森 健(建築士)</div>
    </div>
  </aside>

  <p class="host">主催：マンション管理組合交流会</p>
  <div class="contact-tab"><span>お問合せ</span><span>申し込みは裏面</span></div>
</main>
</body>
</html>
```